Brochure required

Looking at getting business brochure designed for my solar sales company. i will require a range of products to be listed on the brochure I require a simple/ elegent / professional looking brochure.

I am happy to provide designer with all the required information that must go into the brochure. otherwise please visit www.velkariston.com.au and view the products which i would like to allocate into the brochure aswell as our company logo and a little about me section

```html
<!DOCTYPE html>
<html lang="en">
<head>
<meta charset="utf-8">
<title>Velkariston – Brochure Back Cover</title>
<link rel="stylesheet" href="https://fonts.googleapis.com/css2?family=Oswald:wght@400&family=Outfit:wght@400;600&display=swap">
<style>
  :root {
    --brand-blue: #0384b0;
    --brand-green: #00b48a;
    --brand-yellow: #dfc42f;
    --ink: #0b1a26;
    --paper: #ffffff;
    --edge: #000000;
  }
  html, body {
    margin: 0;
    padding: 0;
    width: 1200px;
    height: 1000px;
    overflow: hidden;
    background: var(--paper);
  }
  .canvas {
    position: relative;
    width: 1200px;
    height: 1000px;
    background: var(--paper);
  }
  .cover {
    position: absolute;
    left: 258px;
    top: 15px;
    width: 684px;
    height: 970px;
  }
  .cover-frame {
    position: absolute;
    inset: 0;
  }
  .contact-block {
    position: absolute;
    left: 155px;
    top: 385px;
    padding-left: 42px;
  }
  .contact-rule {
    position: absolute;
    left: 0;
    top: 0;
    width: 10px;
    height: 108px;
    background: var(--ink);
  }
  .contact-line {
    margin: 0;
    font-family: "Oswald", sans-serif;
    font-weight: 400;
    font-size: 32px;
    line-height: 45px;
    letter-spacing: 3px;
    color: var(--ink);
    white-space: nowrap;
  }
  .contact-line.phone { margin-top: 6px; }
  .brand-signoff {
    position: absolute;
    right: 44px;
    top: 808px;
    text-align: right;
    font-family: "Outfit", sans-serif;
    color: var(--ink);
  }
  .brand-name {
    display: flex;
    align-items: center;
    justify-content: flex-end;
    gap: 10px;
    margin: 0;
    font-weight: 600;
    font-size: 40px;
    line-height: 48px;
  }
  .brand-mark {
    width: 26px;
    height: 26px;
    background: var(--brand-green);
    border-radius: 4px;
  }
  .brand-tagline {
    margin: 0;
    font-weight: 400;
    font-size: 16px;
    line-height: 17px;
    letter-spacing: 0.3px;
  }
</style>
</head>
<body>
<main class="canvas">
  <section class="cover">
    <svg class="cover-frame" width="684" height="970" viewBox="0 0 684 970" aria-hidden="true">
      <rect x="0" y="0" width="684" height="970" fill="var(--paper)"/>
      <path d="M682 0 V969 M0 969 H682 M1 0 V969" stroke="var(--edge)" stroke-width="2" fill="none"/>
      <rect class="band-top" x="48" y="0" width="634" height="45" fill="var(--brand-blue)"/>
      <rect class="band-side" x="2" y="40" width="46" height="890" fill="var(--brand-green)"/>
      <path class="corner-top" d="M2 0 H48 V45 H16 A14 14 0 0 1 2 31 Z" fill="var(--brand-yellow)"/>
      <path class="corner-top-round" d="M2 14 A14 14 0 0 1 16 0 H2 Z" fill="var(--paper)"/>
      <path class="band-bottom" d="M48 924 H674 A8 8 0 0 1 682 932 V967 H48 Z" fill="var(--brand-yellow)"/>
      <path class="corner-bottom" d="M16 924 H48 V953 A14 14 0 0 1 34 967 H2 V938 A14 14 0 0 1 16 924 Z" fill="var(--brand-blue)"/>
    </svg>

    <div class="contact-block">
      <span class="contact-rule"></span>
      <p class="contact-line phone">0412 555 019</p>
      <p class="contact-line web">www.velkariston.com.au</p>
    </div>

    <div class="brand-signoff">
      <p class="brand-name"><span class="brand-mark"></span>Velkariston</p>
      <p class="brand-tagline">clean power made simple<br>for brighter homes</p>
    </div>
  </section>
</main>
</body>
</html>
```